Breezella Icons

Icons we would like submitted:

Home
Menu
Shop
Members
Contact
Join the team
Classes
Specials
On the go
Parties

I want simple and sleek there is a company called petal and comb in Houston Texas, we really love their icons, these are good examples. We like the outline look these have. We are also a blow dry bar - NO SCISSORS, NO COLOR APPLICATION, JUST BLOW DRYS AND ALCOHOL.

Please feel free to be excited creative and fun!!
Updates

As soon as I get submissions I will give feedback and accept as soon as I am happy.

Target Market(s)

high end women

Industry/Entity Type

It Company

Requirements
Must have
• cute
Should not have
• succors

```html
<!DOCTYPE html>
<html lang="en">
<head>
<meta charset="utf-8">
<title>Breezella Icons</title>
<link rel="stylesheet" href="https://fonts.googleapis.com/css2?family=Noto+Sans:wght@400;600&display=swap">
<style>
  :root {
    --bg: #f4f4f4;
    --brand: #56c5d1;
    --label: #333a3d;
  }
  * { margin: 0; padding: 0; box-sizing: border-box; }
  html, body { width: 1200px; height: 675px; overflow: hidden; background: var(--bg); }
  .board { position: relative; width: 1200px; height: 675px; font-family: "Noto Sans", sans-serif; }
  .brand-name {
    position: absolute; left: 500px; top: 108px; width: 246px;
    text-align: center; font-size: 36px; font-weight: 600; color: var(--brand);
    letter-spacing: 0.3px; line-height: 1;
  }
  .nav-item { position: absolute; width: 160px; margin-left: -80px; text-align: center; }
  .nav-item svg {
    display: block; margin: 0 auto; width: 44px; height: 44px;
    fill: none; stroke: var(--brand); stroke-width: 1.8; stroke-linecap: round; stroke-linejoin: round;
  }
  .nav-label { display: block; margin-top: 12px; font-size: 14.5px; font-weight: 400; color: var(--label); }
  .row-top { top: 212px; }
  .row-bottom { top: 335px; }
</style>
</head>
<body>
<main class="board">
  <div class="brand-name">Breezella</div>

  <div class="nav-item row-top" style="left:263px">
    <svg viewBox="0 0 48 48"><path d="M5 25 L24 8 L43 25"/><path d="M10 21 V42 H38 V21"/><path d="M20 42 V31 H28 V42"/><path d="M34 16 V9 H38 V19.5"/></svg>
    <span class="nav-label">Home</span>
  </div>
  <div class="nav-item row-top" style="left:425px">
    <svg viewBox="0 0 48 48"><rect x="5" y="5" width="15" height="15"/><rect x="28" y="5" width="15" height="15"/><rect x="5" y="28" width="15" height="15"/><rect x="28" y="28" width="15" height="15"/></svg>
    <span class="nav-label">Menu</span>
  </div>
  <div class="nav-item row-top" style="left:600px">
    <svg viewBox="0 0 48 48"><rect x="4" y="3" width="40" height="42"/><path d="M4 9 H44"/><path d="M4 9 V14 a3.3 3 0 0 0 6.6 0 a3.3 3 0 0 0 6.6 0 a3.3 3 0 0 0 6.6 0 a3.3 3 0 0 0 6.6 0 a3.3 3 0 0 0 6.6 0 a3.3 3 0 0 0 6.6 0 V9"/><rect x="9" y="24" width="19" height="8"/><rect x="33" y="24" width="7" height="17"/><path d="M4 41 H44"/></svg>
    <span class="nav-label">Shop</span>
  </div>
  <div class="nav-item row-top" style="left:757px">
    <svg viewBox="0 0 48 48"><circle cx="24" cy="7" r="4"/><path d="M18 46 V15 H30 V46 M24 30 V46"/><circle cx="12" cy="15" r="3.5"/><path d="M7 46 V22 H17 V46 M12 34 V46"/><circle cx="36" cy="15" r="3.5"/><path d="M31 46 V22 H41 V46 M36 34 V46"/></svg>
    <span class="nav-label">Members</span>
  </div>
  <div class="nav-item row-top" style="left:920px">
    <svg viewBox="0 0 48 48"><path d="M10 7 L15 5 L21 15 L17 19 C19 25 24 30 30 32 L34 28 L43 35 L41 40 C37 44 30 43 23 37 C15 30 9 23 7 16 C6 12 7 9 10 7 Z"/></svg>
    <span class="nav-label">Contact</span>
  </div>

  <div class="nav-item row-bottom" style="left:263px">
    <svg viewBox="0 0 48 48"><circle cx="18" cy="13" r="7"/><circle cx="34" cy="17" r="5"/><path d="M6 38 C6 28 12 24 18 24 C24 24 30 28 30 38 Z"/><path d="M26 27 C28 25 31 25 34 25 C40 25 43 30 43 34 C43 40 36 42 24 40"/></svg>
    <span class="nav-label">Join the Team</span>
  </div>
  <div class="nav-item row-bottom" style="left:425px">
    <svg viewBox="0 0 48 48"><path d="M4 15 C4 10 8 8 12 8 L35 10 L35 22 L18 23 C12 23 4 21 4 15 Z"/><circle cx="11" cy="15" r="3"/><path d="M35 8 L39 6 V26 L35 24"/><path d="M14 23 L11 40 C11 42 13 43 16 43 L18 43 L20 23"/><path d="M42 9 L46 6 M43 16 H47 M42 22 L46 25"/></svg>
    <span class="nav-label">Classes</span>
  </div>
  <div class="nav-item row-bottom" style="left:600px">
    <svg viewBox="0 0 48 48"><rect x="5" y="13" width="38" height="8"/><rect x="8" y="21" width="32" height="23"/><path d="M20 13 V44 M28 13 V44"/><path d="M24 13 C20 5 14 5 15 9 C16 12 22 13 24 13 C26 13 32 12 33 9 C34 5 28 5 24 13"/></svg>
    <span class="nav-label">Specials</span>
  </div>
  <div class="nav-item row-bottom" style="left:757px">
    <svg viewBox="0 0 48 48"><path d="M21 3 H27 L28 8 L33 10 L37 7 L41 11 L38 15 L40 20 L45 21 V27 L40 28 L38 33 L41 37"/><path d="M7 37 L10 33 L8 28 L3 27 V21 L8 20 L10 15 L7 11 L11 7 L15 10 L20 8 L21 3"/><circle cx="24" cy="24" r="12"/><ellipse cx="24" cy="20" rx="4" ry="5"/><path d="M14 44 V35 C14 30 19 28 24 28 C29 28 34 30 34 35 V44 Z M24 30 V40"/></svg>
    <span class="nav-label">On the Go</span>
  </div>
  <div class="nav-item row-bottom" style="left:920px">
    <svg viewBox="0 0 48 48"><path d="M3 20 H21 L12 30 Z"/><path d="M12 30 V44 M8 44 H16"/><path d="M33 2 H37 V10 C40 12 41 14 41 17 V46 H29 V17 C29 14 30 12 33 10 Z"/><rect x="31" y="24" width="8" height="10"/></svg>
    <span class="nav-label">Parties</span>
  </div>
</main>
</body>
</html>
```